I need a business card design for a Boutique Pilates studio.

I would like to see designs similar to the one that I have uploaded.
thinking between two slogans:
'No ordinary place'
'Not so ordinary'

Contact Information for Business Card

Keva Pilates

```html
<!DOCTYPE html>
<html lang="en">
<head>
<meta charset="utf-8">
<title>Keva Pilates – Business Card</title>
<link rel="stylesheet" href="https://fonts.googleapis.com/css2?family=Josefin+Sans:wght@300&family=Great+Vibes&display=swap">
<style>
  :root {
    --backdrop: #2b2b2b;
    --card: #1c1c1d;
    --ink-dark: #0c0c0c;
    --gold: #d7c21a;
    --yellow: #ffe100;
    --text-light: #d9d9d9;
    --rule: #6a6a6a;
  }
  * { margin: 0; padding: 0; box-sizing: border-box; }
  html, body { width: 1200px; height: 689px; overflow: hidden; background: var(--backdrop); }
  .canvas {
    position: relative; width: 1200px; height: 689px;
    display: flex; align-items: center; justify-content: center; gap: 50px;
  }
  .card {
    position: relative; width: 525px; height: 300px;
    background: var(--card); border-radius: 22px; overflow: hidden;
    box-shadow: 0 18px 40px rgba(0,0,0,.45);
  }
  .wordmark {
    font-family: "Josefin Sans", sans-serif; font-weight: 300;
    font-size: 46px; letter-spacing: 1px; white-space: nowrap;
  }

  /* Back face */
  .card--back .brand { position: absolute; left: 0; right: 0; top: 118px; text-align: center; }
  .card--back .wordmark { color: var(--ink-dark); }

  /* Front face */
  .card--front .brand { position: absolute; left: 34px; top: 128px; width: 230px; }
  .card--front .wordmark { color: var(--gold); font-size: 34px; }
  .divider {
    position: absolute; left: 280px; top: 42px; width: 1px; height: 180px;
    background: linear-gradient(to bottom, transparent, var(--rule) 30%, var(--rule) 70%, transparent);
  }
  .contact { position: absolute; left: 302px; top: 36px; color: var(--text-light);
    font-family: "Josefin Sans", sans-serif; font-weight: 300; }
  .person-name { font-family: "Great Vibes", cursive; color: var(--gold); font-size: 34px; line-height: 1; }
  .person-role { font-size: 15px; margin-top: 2px; margin-bottom: 16px; }
  .contact-list { list-style: none; font-size: 12.5px; }
  .contact-list li { display: flex; align-items: center; gap: 9px; height: 22px; }
  .contact-list svg { width: 15px; height: 15px; flex: none; }
  .highlight { color: var(--gold); }
  .address { font-size: 12.5px; margin-top: 12px; line-height: 1.5; padding-left: 24px; }
  .band-rule { position: absolute; left: 0; right: 0; bottom: 34px; height: 2px; background: var(--gold); }
  .band {
    position: absolute; left: 0; right: 0; bottom: 0; height: 26px;
    background: linear-gradient(to bottom, #fff04a, var(--yellow) 45%, #d8b800);
  }
</style>
</head>
<body>
<main class="canvas">
  <section class="card card--back" aria-label="Card back">
    <div class="brand">
      <div class="wordmark">Keva Pilates</div>
    </div>
  </section>

  <section class="card card--front" aria-label="Card front">
    <div class="brand">
      <div class="wordmark">Keva Pilates</div>
    </div>
    <div class="divider"></div>
    <div class="contact">
      <div class="person-name">Mara Ellison</div>
      <div class="person-role">Managing Director</div>
      <ul class="contact-list">
        <li>
          <svg viewBox="0 0 16 16" aria-hidden="true"><path fill="var(--gold)" d="M3.5 1.5l2.5 3-1.5 1.6c.9 2 2.4 3.5 4.4 4.4L10.5 9l3 2.5-1.4 2.6C6.5 14 2 9.5 1 3.9z"/></svg>
          044-310 872 516
        </li>
        <li>
          <svg viewBox="0 0 16 16" aria-hidden="true"><rect x="1" y="3.5" width="14" height="9" fill="var(--gold)"/><path d="M1 3.5l7 5.5 7-5.5" fill="none" stroke="var(--card)" stroke-width="1.2"/></svg>
          info@kevastudio.com
        </li>
        <li>
          <svg viewBox="0 0 16 16" aria-hidden="true"><g fill="none" stroke="var(--gold)" stroke-width="1.3"><circle cx="8" cy="8" r="6.3"/><ellipse cx="8" cy="8" rx="2.8" ry="6.3"/><path d="M1.7 8h12.6M2.8 4.8h10.4M2.8 11.2h10.4"/></g></svg>
          <span>www.<span class="highlight">kevastudio</span>.com</span>
        </li>
      </ul>
      <p class="address">421, Address line goes here<br>45452, Country Name</p>
    </div>
    <div class="band-rule"></div>
    <div class="band"></div>
  </section>
</main>
</body>
</html>
```